OLU58 biz card & Stationery

LU58 is a personalized shopping experience brought to you, that lets you find and discover fashion goods through a collection of boutiques curated by taste-makers - celebrities, stylists, designers, and fashion bloggers. Boutiques uses visual technology to help fashionistas discover and shop their look and creates the opportunity for designers to showcase their collections and latest inspirations online.

OLU58 is built on technology developed by our team of fashion experts who work with engineers to “teach” our computer systems to understand various patterns, pairings, and genre definitions. When signed into your account, OLU58 learns about your style and preferences and in turn, provides you better results and recommendations over time. Ultimately, OLU58 will provide shoppers with a much richer and interactive shopping experience and help drive traffic to retailers' websites.

We need a definitely cool business card. The card must be black! And must use our official logo which can be download from OLU58.com

The address for Letter head and evenlop, please use 4872 Crestwick Parkway, Sutie 510 Los Angeles CA90412, email will be anyone@OLU58.com, website is www.OLU58.com

thanks

We received some of the design, thanks. But most of the design are not what we want. We need a very clean version with black ground, you may also use some dark gray to add the element. please take a look at http://morvalstudio.no/work/#pelter__ostrama/, we do like this kind of design very much. hope it help.

```html
<!DOCTYPE html>
<html lang="en">
<head>
<meta charset="utf-8">
<title>OLU58 — Business Card</title>
<link rel="stylesheet" href="https://fonts.googleapis.com/css2?family=Marcellus&family=Roboto+Condensed:wght@300;400&display=swap">
<style>
  :root {
    --page: #ffffff;
    --card: #222222;
    --band-light: #3f3f3f;
    --band-dark: #2c2c2c;
    --ink: #ffffff;
    --ink-muted: #b4b4b4;
  }
  html, body {
    margin: 0;
    padding: 0;
    width: 1200px;
    height: 900px;
    overflow: hidden;
    background: var(--page);
  }
  .canvas {
    position: relative;
    width: 1200px;
    height: 900px;
  }
  .card {
    position: absolute;
    top: 290px;
    width: 441px;
    height: 286px;
  }
  .card svg { position: absolute; inset: 0; }
  .card--front { left: 86px; }
  .card--back { left: 673px; }

  .brand-name {
    position: absolute;
    left: 46px;
    top: 95px;
    margin: 0;
    font-family: "Roboto Condensed", "Arial Narrow", sans-serif;
    font-weight: 300;
    font-size: 60px;
    line-height: 1;
    letter-spacing: 2px;
    color: var(--ink);
  }
  .brand-tagline {
    position: absolute;
    left: 48px;
    top: 171px;
    margin: 0;
    font-family: "Marcellus", "Optima", serif;
    font-size: 14.5px;
    letter-spacing: 0.6px;
    color: var(--ink-muted);
  }
  .contact {
    position: absolute;
    left: 193px;
    top: 102px;
    margin: 0;
    font-family: "Roboto Condensed", "Arial Narrow", sans-serif;
    font-weight: 300;
    font-size: 15.5px;
    line-height: 16px;
    color: var(--ink);
    font-style: normal;
  }
  .contact p { margin: 0 0 16px; }
</style>
</head>
<body>
<main class="canvas">
  <section class="card card--front" aria-label="Business card front">
    <svg width="441" height="286" viewBox="0 0 441 286" aria-hidden="true">
      <defs>
        <linearGradient id="front-band" x1="0" y1="0" x2="1" y2="0">
          <stop offset="0" stop-color="#3f3f3f"/>
          <stop offset="1" stop-color="#2c2c2c"/>
        </linearGradient>
      </defs>
      <path d="M0 286 V40 A40 40 0 0 1 40 0 H441 V286 Z" fill="var(--card)"/>
      <path d="M297 90 H441 V195 H297 Q324 142.5 297 90 Z" fill="url(#front-band)"/>
    </svg>
    <h1 class="brand-name">OLU58</h1>
    <p class="brand-tagline">SOCIAL FASHION ONLINE</p>
  </section>

  <section class="card card--back" aria-label="Business card back">
    <svg width="441" height="286" viewBox="0 0 441 286" aria-hidden="true">
      <defs>
        <linearGradient id="back-band" x1="0" y1="0" x2="1" y2="0">
          <stop offset="0" stop-color="#2c2c2c"/>
          <stop offset="0.35" stop-color="#3f3f3f"/>
          <stop offset="1" stop-color="#222222"/>
        </linearGradient>
      </defs>
      <path d="M0 0 H401 A40 40 0 0 1 441 40 V286 H0 Z" fill="var(--card)"/>
      <rect x="0" y="90" width="170" height="105" fill="url(#back-band)"/>
    </svg>
    <address class="contact">
      <p>4872 Crestwick Parkway, Sutie 510<br>Los Angeles CA90412</p>
      <p>anyone@OLU58.com<br>www.OLU58.com</p>
    </address>
  </section>
</main>
</body>
</html>
```